Display Carton for cinnamon sticks

Display Box Specification – Cerro del Tomillo Cinnamon Sticks
Design a retail-ready display box for Cerro del Tomillo cinnamon sticks, sourced from Sri Lanka. Each selling unit contains two 5" cinnamon sticks, individually sealed in a clear cellophane wrapper to preserve freshness and showcase product quality.
📦 Carton Configuration
• Total Units per Display: 32 wrappers
• Layering Structure: 8 wrappers per layer × 4 layers high
• Orientation: Wrappers laid flat, stacked horizontally for optimal visibility and ease of access
I uploaded 2 AI-generated images for reference purposes only

Target Market(s)

Cultural Appeal Suggestions Color Palette: Use warm, earthy tones like terracotta, deep reds, and golds—colors often associated with Latin American aesthetics. Typography: Consider a bold, rustic font with a handcrafted feel to evoke authenticity. Language: Include bilingual labeling (English & Spanish). For example: “Cinnamon Sticks” → “Palitos de Canela” “Sourced from Sri Lanka” → “Origen: Sri Lanka” Storytelling Element: Add a short cultural or culinary note about how cinnamon is used in Latin cuisine (e.g., in café de olla, arroz con leche, or ponche).

Font styles to use
Other font styles liked:
• Consider a bold, rustic font with a handcrafted feel to evoke authenticity.

Requirements
Nice to have
• 📦 Display Box Messaging Front panel: “Cerro del Tomillo – Premium Canela de Ceilán” (Ceylon Cinnamon – Naturally Sweet & Aromatic) Side panel: “Perfect for traditional recipes and everyday flavor” (Ideal para recetas tradicionales y sabor diario)

```html
<!DOCTYPE html>
<html lang="en">
<head>
<meta charset="utf-8">
<title>Cerro del Tomillo – Cinnamon Sticks Display Carton</title>
<link rel="stylesheet" href="https://fonts.googleapis.com/css2?family=Cinzel:wght@400;700&family=Roboto:wght@400&display=swap">
<style>
  :root {
    --bg: #d6d6d6;
    --saffron: #f2b95a;
    --saffron-deep: #e9a843;
    --saffron-side: #eaa53f;
    --cocoa: #5b2f24;
    --gold: #e8b25c;
    --ink: #1e1a17;
    --stripe-red: #e2553a;
    --stripe-green: #1f8a4c;
  }
  * { box-sizing: border-box; margin: 0; padding: 0; }
  html, body { width: 1200px; height: 800px; overflow: hidden; }
  body {
    background: var(--bg);
    font-family: "Cinzel", serif;
    color: var(--ink);
    position: relative;
  }
  .brand-mark {
    display: inline-block; border-radius: 50%;
    background: var(--ink); vertical-align: middle;
  }

  /* ---------- End panel ---------- */
  .end-panel {
    position: absolute; left: 30px; top: 190px;
    width: 180px; height: 420px;
    background: var(--saffron-side);
    padding: 22px 16px;
  }
  .end-brand { font-weight: 700; font-size: 16px; line-height: 1.1; letter-spacing: 0.5px; }
  .end-brand .brand-mark { width: 9px; height: 9px; margin-right: 5px; }
  .end-product { margin-top: 14px; font-size: 11px; letter-spacing: 1px; }
  .end-count { display: flex; align-items: baseline; gap: 8px; margin-top: 4px; }
  .end-count strong { font-size: 38px; font-weight: 700; line-height: 1; }
  .end-count span { font-size: 11px; letter-spacing: 1px; }
  .end-copy { margin-top: 14px; }
  .end-copy h3 { font-size: 9px; font-weight: 400; letter-spacing: 0.5px; line-height: 1.35; }
  .end-copy hr { border: 0; border-top: 1px solid var(--ink); margin: 8px 0; }
  .end-copy p { font-family: "Roboto", sans-serif; font-size: 9px; line-height: 1.4; margin-bottom: 5px; }
  .end-origin {
    position: absolute; left: 16px; bottom: 20px;
    display: flex; align-items: center; gap: 8px;
  }
  .end-origin .origin-art { width: 50px; height: 38px; }
  .end-origin .origin-text { font-size: 8px; letter-spacing: 2px; line-height: 1.3; }
  .end-origin .origin-text strong { display: block; font-size: 15px; letter-spacing: 0.5px; }

  /* ---------- Lid panel ---------- */
  .lid-panel {
    position: absolute; left: 230px; top: 190px;
    width: 460px; height: 420px;
    background: var(--saffron);
  }
  .lid-brand {
    position: absolute; left: 28px; top: 36px;
    font-weight: 700; font-size: 22px; line-height: 1.08; letter-spacing: 0.5px;
  }
  .lid-brand .brand-mark { width: 12px; height: 12px; margin-right: 7px; }
  .lid-product { position: absolute; left: 28px; top: 108px; font-size: 13px; letter-spacing: 1px; }
  .lid-count { position: absolute; left: 28px; top: 134px; display: flex; align-items: baseline; gap: 10px; }
  .lid-count strong { font-size: 50px; font-weight: 700; line-height: 1; }
  .lid-count span { font-size: 13px; letter-spacing: 1px; }

  .lid-copy { position: absolute; left: 220px; top: 36px; width: 212px; }
  .lid-copy h3 { font-size: 11px; font-weight: 400; letter-spacing: 0.5px; line-height: 1.4; }
  .lid-copy hr { border: 0; border-top: 1.5px solid var(--ink); margin: 12px 0; }
  .lid-copy p { font-family: "Roboto", sans-serif; font-size: 10.5px; line-height: 1.45; margin-bottom: 8px; }
  .lid-origin {
    position: absolute; left: 220px; top: 300px;
    display: flex; align-items: center; gap: 12px;
  }
  .lid-origin .origin-art { width: 80px; height: 60px; }
  .lid-origin .origin-text { font-size: 11px; letter-spacing: 3px; line-height: 1.3; }
  .lid-origin .origin-text strong { display: block; font-size: 22px; letter-spacing: 1px; }

  /* ---------- Front panel ---------- */
  .front-panel {
    position: absolute; left: 710px; top: 190px;
    width: 460px; height: 420px;
    background: var(--cocoa);
    overflow: hidden;
  }
  .front-frame { position: absolute; left: 0; top: 0; width: 460px; height: 280px; }
  .front-window {
    position: absolute; left: 26px; top: 20px; width: 408px; height: 232px;
    background: var(--saffron); border-radius: 18px;
  }
  .front-brand {
    position: absolute; left: 0; right: 0; top: 44px;
    text-align: center; font-weight: 700; font-size: 24px; letter-spacing: 0.5px;
  }
  .front-brand .brand-mark { width: 13px; height: 13px; margin-right: 8px; }
  .sticks-art { position: absolute; left: 185px; top: 98px; width: 90px; height: 122px; }
  .front-word { position: absolute; font-weight: 700; font-size: 20px; letter-spacing: 2px; }
  .word-left { left: 52px; top: 190px; }
  .word-right { right: 52px; top: 122px; }
  .band-art { position: absolute; left: 0; top: 262px; width: 460px; height: 100px; }
  .front-tagline {
    position: absolute; left: 0; right: 0; top: 376px;
    text-align: center; font-size: 12px; letter-spacing: 2px; color: var(--gold);
  }
</style>
</head>
<body>

<section class="end-panel" aria-label="End panel">
  <div class="end-brand"><span class="brand-mark"></span>CERRO<br>DEL TOMILLO</div>
  <div class="end-product">CINNAMON STICKS</div>
  <div class="end-count"><strong>25</strong><span>STICKS</span></div>
  <div class="end-copy">
    <h3>PERFECT FOR TRADITIONAL RECIPES AND EVERYDAY FLAVOR (IDEAL PARA RECETAS TRADICIONALES Y SABOR DIARIO)</h3>
    <hr>
    <p>Lorem ipsum dolor sit amet, consectetur adipiscing elit.</p>
    <p>Pellentesque at elit molestie, gravida dui non.</p>
  </div>
  <div class="end-origin">
    <svg class="origin-art" role="img" aria-label="Engraved illustration of a spice harvest scene" viewBox="0 0 50 38">
      <rect width="50" height="38" rx="4" fill="var(--saffron-deep)"/>
    </svg>
    <div class="origin-text">PREMIUM<br>CANELA DE<strong>CEILÁN</strong></div>
  </div>
</section>

<section class="lid-panel" aria-label="Lid panel">
  <div class="lid-brand"><span class="brand-mark"></span>CERRO<br>DEL TOMILLO</div>
  <div class="lid-product">CINNAMON STICKS</div>
  <div class="lid-count"><strong>25</strong><span>STICKS</span></div>

  <div class="lid-copy">
    <h3>PERFECT FOR TRADITIONAL RECIPES AND EVERYDAY FLAVOR (IDEAL PARA RECETAS TRADICIONALES Y SABOR DIARIO)</h3>
    <hr>
    <p>Lorem ipsum dolor sit amet, consectetur adipiscing elit. Nulla ac sapien non tellus blandit fringilla.</p>
    <p>Pellentesque at elit molestie, gravida dui non, venenatis erat. Proin eget risus eu purus mollis porta.</p>
  </div>

  <div class="lid-origin">
    <svg class="origin-art" role="img" aria-label="Engraved illustration of a spice harvest scene" viewBox="0 0 80 60">
      <rect width="80" height="60" rx="6" fill="var(--saffron-deep)"/>
    </svg>
    <div class="origin-text">PREMIUM<br>CANELA DE<strong>CEILÁN</strong></div>
  </div>
</section>

<section class="front-panel" aria-label="Front panel">
  <svg class="front-frame" viewBox="0 0 460 280" role="img" aria-label="Zigzag border pattern in red, green and blue framing the panel">
    <rect x="14" y="9" width="432" height="254" rx="24" fill="none" stroke="var(--stripe-red)" stroke-width="10"/>
    <rect x="14" y="9" width="432" height="254" rx="24" fill="none" stroke="var(--stripe-green)" stroke-width="4"/>
  </svg>
  <div class="front-window"></div>

  <div class="front-brand"><span class="brand-mark"></span>CERRO DEL TOMILLO</div>
  <svg class="sticks-art" role="img" aria-label="Photograph of tied cinnamon sticks" viewBox="0 0 90 122">
    <defs>
      <linearGradient id="stickTone" x1="0" y1="0" x2="1" y2="1">
        <stop offset="0" stop-color="#c98a5a"/>
        <stop offset="1" stop-color="#8f5532"/>
      </linearGradient>
    </defs>
    <rect width="90" height="122" rx="8" fill="url(#stickTone)"/>
  </svg>
  <div class="front-word word-left">CINAMON</div>
  <div class="front-word word-right">STICKS</div>

  <svg class="band-art" role="img" aria-label="Gold ornamental fan and leaf pattern on a cocoa band" viewBox="0 0 460 100">
    <defs>
      <linearGradient id="bandTone" x1="0" y1="0" x2="0" y2="1">
        <stop offset="0" stop-color="#6e3d2a"/>
        <stop offset="0.5" stop-color="#8a5b34"/>
        <stop offset="1" stop-color="#5b2f24"/>
      </linearGradient>
    </defs>
    <rect width="460" height="100" fill="url(#bandTone)"/>
  </svg>
  <div class="front-tagline">PREMIUM CANELA DE CEILÁN</div>
</section>

</body>
</html>
```